Willowbend Spine Chiropractic

office phone- 913-462-1037
After Hour number 913-284-6150
Office address 27814 Halvorn Rd. Overland Park Ks 66947
Dr. Marlon Pettigrew, DC
I added 3 different types of logos proofs.
Specalizing in:
Family Wellness Care
Auto Accident
Workman Comp Injuries
Urgent Alternative Pain Relief
Non-operative Sports Injury Care

```html
<!DOCTYPE html>
<html lang="en">
<head>
<meta charset="utf-8">
<title>Willowbend Spine Chiropractic – Business Card</title>
<link rel="stylesheet" href="https://fonts.googleapis.com/css2?family=Source+Sans+3:ital,wght@0,400;0,600;0,700;1,400&display=swap">
<style>
  :root {
    --navy: #2a2c7c;
    --red: #e5432d;
    --paper: #f7f7f8;
    --paper-shade: #e9e9ec;
    --photo-dark: #141414;
    --photo-mid: #3b3b3d;
    --photo-light: #8d8d90;
  }
  * { margin: 0; padding: 0; box-sizing: border-box; }
  html, body {
    width: 1200px;
    height: 702px;
    overflow: hidden;
    background: var(--paper);
  }
  .card {
    position: relative;
    width: 1200px;
    height: 702px;
    overflow: hidden;
    font-family: "Source Sans 3", "Myriad Pro", Arial, sans-serif;
    color: var(--navy);
    background: radial-gradient(ellipse at 80% 40%, #ffffff 0%, var(--paper) 55%, var(--paper-shade) 100%);
  }
  .card p, .card h1, .card address, .card li { line-height: 1; white-space: nowrap; }
  .back-photo {
    position: absolute;
    left: 0;
    top: 0;
    width: 640px;
    height: 702px;
    background:
      radial-gradient(ellipse 70px 360px at 250px 370px, rgba(200,200,204,0.55) 0%, rgba(200,200,204,0) 100%),
      linear-gradient(90deg, var(--photo-dark) 0%, var(--photo-mid) 35%, var(--photo-dark) 62%, var(--photo-light) 82%, rgba(247,247,248,0) 100%);
  }
  .brand {
    position: absolute;
    left: 588px;
    top: 48px;
    font-size: 42px;
    font-weight: 700;
    line-height: 1;
    color: var(--navy);
    white-space: nowrap;
  }
  .doctor {
    position: absolute;
    left: 553px;
    top: 186px;
    font-size: 51px;
    font-weight: 600;
  }
  .address {
    position: absolute;
    left: 554px;
    top: 255px;
    font-size: 40px;
    font-weight: 400;
    font-style: normal;
  }
  .address span { display: block; line-height: 44px; }
  .phone {
    position: absolute;
    left: 554px;
    top: 366px;
    font-size: 42px;
    color: var(--red);
  }
  .after-hours {
    position: absolute;
    left: 554px;
    top: 409px;
    font-size: 35px;
    font-style: italic;
  }
  .specialties-label {
    position: absolute;
    left: 558px;
    top: 472px;
    font-size: 34px;
  }
  .specialties {
    position: absolute;
    left: 796px;
    top: 472px;
    list-style: none;
    font-size: 25px;
  }
  .specialties li { line-height: 37px; }
</style>
</head>
<body>
  <div class="card">
    <div class="back-photo" role="img" aria-label="Black and white photo of a person's back with the spine highlighted in white"></div>

    <div class="brand">Willowbend Spine Chiropractic</div>

    <h1 class="doctor">Dr. Marlon Pettigrew, DC</h1>

    <address class="address">
      <span>27814 Halvorn Rd.</span>
      <span>Overland Park, KS 66947</span>
    </address>

    <p class="phone">Office: 913-462-1037</p>
    <p class="after-hours">*after hours number* 913-284-6150</p>

    <p class="specialties-label">Specializing in:</p>
    <ul class="specialties">
      <li>Family Wellness Care</li>
      <li>Auto Accident</li>
      <li>Workman Comp Injuries</li>
      <li>Urgent Alternative Pain Relief</li>
      <li>Non-operative Sports Injury Care</li>
    </ul>
  </div>
</body>
</html>
```